Pemberton Dialworks Business Card Design

Double Sided Business Card Design for a Locksmith company specializing in Safecracking, safe & vault service.

```html
<!DOCTYPE html>
<html lang="en">
<head>
<meta charset="utf-8">
<title>Pemberton Dialworks Business Card</title>
<link href="https://fonts.googleapis.com/css2?family=Open+Sans:wght@300;600;700&display=swap" rel="stylesheet">
<style>
  :root {
    --page-bg: #1a1a1a;
    --card-bg: #2b2b2b;
    --brand-green: #217a3c;
    --text-white: #ffffff;
    --text-soft: #e6e6e6;
  }
  html, body {
    margin: 0;
    padding: 0;
    width: 1200px;
    height: 1200px;
    overflow: hidden;
    background: var(--page-bg);
    font-family: "Open Sans", Arial, sans-serif;
  }
  .card {
    position: absolute;
    left: 215px;
    width: 770px;
    height: 440px;
    background: var(--card-bg);
  }
  .card--front { top: 135px; }
  .card--back { top: 611px; }

  .brand {
    position: absolute;
    left: 0;
    right: 0;
    top: 190px;
    display: flex;
    align-items: center;
    justify-content: center;
    gap: 18px;
  }
  .brand__dot {
    width: 62px;
    height: 62px;
    border-radius: 50%;
    background: var(--brand-green);
    flex: none;
  }
  .brand__name {
    font-weight: 700;
    font-size: 40px;
    letter-spacing: 0.5px;
    color: var(--brand-green);
    white-space: nowrap;
  }

  .name-band {
    position: absolute;
    left: 211px;
    top: 178px;
    width: 348px;
    height: 62px;
    border-radius: 31px;
    background: var(--brand-green);
    display: flex;
    align-items: center;
    justify-content: center;
  }
  .name-band__name {
    font-weight: 600;
    font-size: 43px;
    line-height: 1;
    color: var(--text-white);
    white-space: nowrap;
  }
  .contact {
    position: absolute;
    left: 0;
    right: 0;
    top: 252px;
    text-align: center;
    color: var(--text-soft);
    font-size: 17px;
    font-weight: 300;
    line-height: 1;
  }
  .contact__address { margin: 0; }
  .contact__divider {
    width: 64px;
    height: 1px;
    background: var(--brand-green);
    margin: 17px auto 8px;
    border: 0;
  }
  .contact__line { margin: 0 0 7px; }
  .contact__label { font-weight: 700; color: var(--text-white); }
  .contact__sep { margin: 0 6px; }
  .contact__web {
    margin: 0;
    font-weight: 700;
    color: var(--text-white);
    font-size: 17px;
  }
</style>
</head>
<body>
  <section class="card card--front" aria-label="Card front">
    <div class="brand">
      <span class="brand__dot" aria-hidden="true"></span>
      <span class="brand__name">Pemberton Dialworks</span>
    </div>
  </section>

  <section class="card card--back" aria-label="Card back">
    <div class="name-band">
      <span class="name-band__name">Owen Hartley</span>
    </div>
    <div class="contact">
      <p class="contact__address">480 Alder Row, Suite 12 Fairbrook , OR , 97402</p>
      <hr class="contact__divider">
      <p class="contact__line"><span class="contact__label">t:</span> 555-014-2290<span class="contact__sep">|</span><span class="contact__label">e:</span> hello@pembertondial.com</p>
      <p class="contact__web">www.pembertondialworks.com</p>
    </div>
  </section>
</body>
</html>
```